Town's Facebook Cover Photo / Banner

We are launching a new town Facebook Page. The name of the page is:
The Fernwicker , its is intended to be the digiatal "town square" for the residence of Fernwick, a very quaint suburan town in NJ.

Would like the words "Town Squre" to be prominent displayed on the Cover photo

Also need to include our Slogan: "Your Community, Your Future, Your Fernwick!"

Target Market(s)

The local Towns People of Fernwick Only

Number of Pages Required

1 page

Requirements
Must have
• The Fernwicker Prominently Displayed

```html
<!DOCTYPE html>
<html lang="en">
<head>
<meta charset="utf-8">
<title>The Fernwicker – Town Square Cover</title>
<link rel="stylesheet" href="https://fonts.googleapis.com/css2?family=Playfair+Display:wght@700&family=Poppins:ital,wght@0,400;0,500;1,600&display=swap">
<style>
  :root {
    --ink-white: #ffffff;
    --slogan-red: #e3141b;
    --tick-red: #e0141c;
    --plaza-dark: #2a2f2c;
    --plaza-mid: #4e5a52;
    --tree-green: #3f5a34;
    --fade-white: #ffffff;
    --badge-purple: #7a5aa6;
    --badge-ink: #3b2f55;
  }
  * { margin: 0; padding: 0; box-sizing: border-box; }
  html, body { width: 1200px; height: 522px; overflow: hidden; background: #fff; }
  .cover {
    position: relative;
    width: 1200px;
    height: 522px;
    overflow: hidden;
    font-family: "Poppins", Arial, sans-serif;
    color: var(--ink-white);
  }
  .cover__scene {
    position: absolute;
    inset: 0;
    background:
      radial-gradient(ellipse 420px 160px at 640px 190px, rgba(90,110,95,0.55), transparent 70%),
      radial-gradient(ellipse 520px 220px at 650px 330px, #6a6f6c 0%, #4e5450 55%, transparent 80%),
      linear-gradient(180deg, var(--tree-green) 0%, var(--plaza-mid) 45%, #5d625f 75%, #7c807d 100%);
  }
  .cover__shade {
    position: absolute;
    inset: 0;
    background: linear-gradient(90deg, rgba(20,22,20,0.55) 0%, rgba(20,22,20,0.25) 45%, rgba(20,22,20,0.1) 100%);
  }
  .cover__fade {
    position: absolute;
    left: 0; right: 0; bottom: 0;
    height: 110px;
    background: linear-gradient(180deg, rgba(255,255,255,0) 0%, rgba(255,255,255,0.7) 50%, var(--fade-white) 85%);
  }
  .masthead { position: absolute; left: 59px; top: 54px; }
  .masthead__title {
    font-family: "Playfair Display", "Times New Roman", serif;
    font-weight: 700;
    font-size: 51px;
    letter-spacing: 0.5px;
    line-height: 1;
    text-transform: uppercase;
  }
  .masthead__sub {
    margin-top: 22px;
    font-size: 31px;
    font-weight: 400;
    line-height: 1;
  }
  .slogan-disc {
    position: absolute;
    left: 878px; top: -88px;
    width: 350px; height: 350px;
    border-radius: 50%;
    background: var(--slogan-red);
  }
  .slogan {
    position: absolute;
    left: 924px; top: 38px;
    font-style: italic;
    font-weight: 600;
    font-size: 25px;
    line-height: 36px;
  }
  .values { position: absolute; left: 307px; top: 252px; }
  .values__lead { font-size: 22px; font-weight: 400; margin-bottom: 10px; }
  .values__list {
    list-style: none;
    display: grid;
    grid-template-columns: 483px auto;
    row-gap: 9px;
  }
  .values__item {
    display: flex;
    align-items: center;
    gap: 14px;
    font-size: 24px;
    font-weight: 500;
    line-height: 32px;
  }
  .values__tick { width: 20px; height: 18px; flex: none; }
  .badge {
    position: absolute;
    left: 24px; top: 299px;
    width: 237px; height: 240px;
    background: #fff;
    border-radius: 8px 8px 0 0;
    display: flex;
    flex-direction: column;
    align-items: center;
    justify-content: center;
    gap: 14px;
  }
  .badge__circle {
    width: 70px; height: 70px;
    border-radius: 50%;
    border: 3px solid var(--badge-purple);
  }
  .badge__name {
    font-family: "Poppins", Arial, sans-serif;
    font-weight: 500;
    font-size: 20px;
    line-height: 26px;
    color: var(--badge-ink);
    text-align: center;
    margin-bottom: 20px;
  }
</style>
</head>
<body>
  <header class="cover">
    <div class="cover__scene" role="img" aria-label="Aerial evening photo of a busy town square with trees, paths and people gathering around a central plaza"></div>
    <div class="cover__shade"></div>
    <div class="cover__fade"></div>

    <div class="slogan-disc"></div>
    <p class="slogan">Your Community,<br>Your Future,<br>Your Fernwick!</p>

    <div class="masthead">
      <h1 class="masthead__title">The Fernwicker</h1>
      <p class="masthead__sub">Town Square</p>
    </div>

    <section class="values">
      <p class="values__lead">We believe in:</p>
      <ul class="values__list">
        <li class="values__item"><svg class="values__tick" viewBox="0 0 20 18"><path d="M2 10 L7.5 15 L18 3" fill="none" stroke="var(--tick-red)" stroke-width="4" stroke-linecap="round" stroke-linejoin="round"/></svg>Community Involvement</li>
        <li class="values__item"><svg class="values__tick" viewBox="0 0 20 18"><path d="M2 10 L7.5 15 L18 3" fill="none" stroke="var(--tick-red)" stroke-width="4" stroke-linecap="round" stroke-linejoin="round"/></svg>Shared Traditions</li>
        <li class="values__item"><svg class="values__tick" viewBox="0 0 20 18"><path d="M2 10 L7.5 15 L18 3" fill="none" stroke="var(--tick-red)" stroke-width="4" stroke-linecap="round" stroke-linejoin="round"/></svg>Free Speech and Healthy Debate</li>
        <li class="values__item"><svg class="values__tick" viewBox="0 0 20 18"><path d="M2 10 L7.5 15 L18 3" fill="none" stroke="var(--tick-red)" stroke-width="4" stroke-linecap="round" stroke-linejoin="round"/></svg>Collaboration</li>
        <li class="values__item"><svg class="values__tick" viewBox="0 0 20 18"><path d="M2 10 L7.5 15 L18 3" fill="none" stroke="var(--tick-red)" stroke-width="4" stroke-linecap="round" stroke-linejoin="round"/></svg>Respect and Kindness</li>
        <li class="values__item"><svg class="values__tick" viewBox="0 0 20 18"><path d="M2 10 L7.5 15 L18 3" fill="none" stroke="var(--tick-red)" stroke-width="4" stroke-linecap="round" stroke-linejoin="round"/></svg>Community Spirit:</li>
      </ul>
    </section>

    <div class="badge">
      <div class="badge__circle"></div>
      <p class="badge__name">Fernwick<br>Town Square</p>
    </div>
  </header>
</body>
</html>
```